Len Morvath

I am the director of Casa Del Humo International. We make premium cigars

I want an insanely beautiful card that directly attracts attention. Do your best. The card can use emboss, foil, laser-cut metal or anything else. Make it stand out, but also elegant.

Target Market(s)

Cigar Distributors

Industry/Entity Type

Cigars

Contact Information for Business Card

Email: len.morvath@morvaths.com + Logos (attached) + Position: Director + 'High-End Cigars'

Colors

Designer to choose colors to be used in the design.

Requirements
Nice to have
• Please check us out at www.casadelhumo.com and try to use our colors and styles

```html
<!DOCTYPE html>
<html lang="en">
<head>
<meta charset="utf-8">
<title>Casa Del Humo International – Business Card</title>
<link href="https://fonts.googleapis.com/css2?family=EB+Garamond:wght@400;500;700&family=Arimo:wght@400&display=swap" rel="stylesheet">
<style>
  :root {
    --stage: #1b1b1b;
    --card-light: #f3f3f3;
    --card-dark: #1f1f1f;
    --ink: #1e1e1e;
    --ink-soft: #333333;
    --paper-text: #f4f4f4;
    --accent-red: #c1272d;
    --brand-red: #9e1b24;
    --brand-gold: #b59a5e;
    --brand-brown: #6b3a22;
  }
  * { margin: 0; padding: 0; box-sizing: border-box; }
  html, body { width: 1200px; height: 1059px; overflow: hidden; }
  body {
    position: relative;
    background: var(--stage);
    font-family: "Arimo", Arial, sans-serif;
  }
  .card {
    position: absolute;
    border-radius: 20px;
    overflow: hidden;
  }
  .card--front { left: 256px; top: 89px; width: 688px; height: 390px; background: var(--card-light); color: var(--ink); }
  .card--back  { left: 254px; top: 547px; width: 693px; height: 393px; background: var(--card-dark); color: var(--paper-text); }

  .company {
    position: absolute; left: 0; right: 0; text-align: center;
    font-family: "EB Garamond", Georgia, serif; font-weight: 500;
    letter-spacing: 0.2px; white-space: nowrap;
  }
  .card--front .company { top: 52px; font-size: 25px; }
  .card--back .company { top: 62px; font-size: 30px; }

  .divider { position: absolute; height: 12px; }
  .divider::before {
    content: ""; position: absolute; left: 0; right: 0; top: 5.5px; height: 1px; background: var(--accent-red);
  }
  .divider::after {
    content: ""; position: absolute; left: 50%; top: 1px; width: 9px; height: 9px;
    margin-left: -4.5px; background: var(--accent-red); transform: rotate(45deg);
  }
  .card--front .divider { left: 124px; width: 440px; top: 87px; }
  .card--back .divider { left: 67px; width: 559px; top: 105px; }

  .location { position: absolute; left: 0; right: 0; text-align: center; letter-spacing: 0.2px; }
  .card--front .location { top: 105px; font-size: 16px; }
  .card--back .location { top: 126px; font-size: 20px; }

  .person { position: absolute; right: 364px; top: 196px; text-align: right; white-space: nowrap; }
  .person__name {
    font-family: "EB Garamond", Georgia, serif; font-weight: 700;
    font-size: 28px; color: var(--accent-red); line-height: 1;
  }
  .person__role { font-size: 17px; color: var(--ink-soft); margin-top: 4px; }

  .rule-vertical { position: absolute; left: 344px; top: 187px; width: 1px; height: 67px; background: var(--accent-red); }

  .contacts { position: absolute; left: 362px; top: 183px; list-style: none; }
  .contacts li { display: flex; align-items: center; height: 27px; font-size: 17px; color: var(--ink-soft); white-space: nowrap; }
  .contacts svg { width: 13px; height: 13px; margin-right: 8px; flex: none; }

  .address { position: absolute; left: 0; right: 0; top: 311px; text-align: center; font-size: 17px; color: var(--ink-soft); }

  .brands { position: absolute; left: 0; right: 0; top: 250px; height: 50px; }
  .brand {
    position: absolute; top: 0; transform: translateX(-50%);
    display: flex; align-items: center;
    font-family: "EB Garamond", Georgia, serif; font-weight: 500; font-size: 26px; white-space: nowrap;
    height: 50px;
  }
  .brand--corvanta { left: 149px; color: var(--brand-red); }
  .brand--bellmoor { left: 338px; color: var(--brand-gold); }
  .brand--tierra { left: 532px; color: var(--brand-brown); }
</style>
</head>
<body>

<section class="card card--front">
  <h1 class="company">CASA DEL HUMO INTERNATIONAL</h1>
  <div class="divider"></div>
  <p class="location">MIRASOL - VALLERANA</p>

  <div class="person">
    <p class="person__name">LEN MORVATH</p>
    <p class="person__role">Director + 'High-End Cigars</p>
  </div>
  <div class="rule-vertical"></div>

  <ul class="contacts">
    <li>
      <svg viewBox="0 0 16 16" aria-hidden="true"><path fill="#c1272d" d="M3.5 1.5l2.5 3-1.5 1.5c.8 1.8 2.2 3.2 4 4l1.5-1.5 3 2.5-1.5 2.5C7 13 3 9 1 3.5z"/></svg>
      (555)-214-3068
    </li>
    <li>
      <svg viewBox="0 0 16 16" aria-hidden="true"><rect x="1" y="4" width="14" height="10" fill="#c1272d"/><path d="M1 4l7 5 7-5" fill="none" stroke="#f3f3f3" stroke-width="1.2"/></svg>
      len.morvath@morvaths.com
    </li>
    <li>
      <svg viewBox="0 0 16 16" aria-hidden="true"><circle cx="8" cy="8" r="7" fill="#c1272d"/><path d="M8 1v14M1 8h14M3 4c3 1.5 7 1.5 10 0M3 12c3-1.5 7-1.5 10 0" fill="none" stroke="#f3f3f3" stroke-width="0.9"/></svg>
      www.casadelhumo.com
    </li>
  </ul>

  <p class="address">14720, Barrio Las Ceibas Calle Central, Monte Verano.</p>
</section>

<section class="card card--back">
  <h2 class="company">CASA DEL HUMO INTERNATIONAL</h2>
  <div class="divider"></div>
  <p class="location">MIRASOL - VALLERANA</p>

  <div class="brands">
    <span class="brand brand--corvanta">Corvanta</span>
    <span class="brand brand--bellmoor">Bellmoor</span>
    <span class="brand brand--tierra">Tierra Norte</span>
  </div>
</section>

</body>
</html>
```